Medical Transportation Company Brochure

I need a brochure for a medical transportation company called CareSwift Transit Health Services that provides ambulance and mobility assistance vehicle transportation services to and from healthcare facilities as well as event standby and healthcare training through our training center (cpr, professional continuing education courses). Id like something that incorporates our company logo's colors and looks eye catching yet sleek and professional

Target Market(s)

Patients, healthcare facilities

Industry/Entity Type

Medical

Font styles to use
Sans Serif

Requirements
Must have
• Flyer must have a description of our services as well as text that is easy to read, be visually captivating and stand out, include our contact information and process to book appointment for transport with us

```html
<!DOCTYPE html>
<html lang="en">
<head>
<meta charset="utf-8">
<title>CareSwift Transit Health Services – Flyer</title>
<link rel="stylesheet" href="https://fonts.googleapis.com/css2?family=Montserrat:wght@400;500;600;700&display=swap">
<style>
  :root {
    --red: #b3001f;
    --navy: #1c3566;
    --navy-deep: #15295a;
    --orange: #f6a833;
    --white: #ffffff;
    --paper: #f1f1f2;
  }
  * { box-sizing: border-box; margin: 0; padding: 0; }
  html, body { width: 848px; height: 1200px; overflow: hidden; background: var(--paper); }
  body { font-family: "Montserrat", Arial, sans-serif; }
  .flyer { position: relative; width: 848px; height: 1200px; overflow: hidden;
    background: linear-gradient(160deg, #ffffff 0%, #ececee 45%, #f5f5f6 100%); }
  .backdrop { position: absolute; inset: 0; }
  .abs { position: absolute; line-height: 1; white-space: nowrap; }

  .brand { left: 29px; top: 44px; display: flex; align-items: center; gap: 14px; }
  .brand-dot { width: 78px; height: 78px; border-radius: 50%; background: var(--navy); }
  .brand-name { color: var(--navy); font-weight: 700; line-height: 1; }
  .brand-name .main { display: block; font-size: 52px; letter-spacing: -1px; }
  .brand-name .sub { display: block; font-size: 15.5px; letter-spacing: 1px; margin-top: 8px; text-transform: uppercase; }

  .headline-we { left: 201px; top: 425px; color: var(--white); font-size: 68px; font-weight: 500; }
  .headline-we .provides { font-size: 38px; font-weight: 600; margin-left: 6px; }
  .headline-main { left: 200px; top: 484px; color: var(--orange); font-size: 71px; font-weight: 700; letter-spacing: -0.5px; }
  .headline-amp { left: 658px; top: 472px; color: var(--orange); font-size: 150px; font-weight: 500; }
  .headline-sub { left: 202px; top: 555px; color: var(--white); font-size: 47px; font-weight: 500; }
  .headline-tag { left: 264px; top: 606px; color: var(--orange); font-size: 29px; font-weight: 600; }

  .service-title { color: var(--white); font-size: 30px; font-weight: 600; }
  .service-note { color: var(--white); font-size: 19px; font-weight: 400; }
  .rule { position: absolute; height: 4px; width: 126px; background: var(--orange); }

  .intro { left: 140px; top: 962px; width: 666px; text-align: center; color: var(--white);
    font-size: 25px; font-weight: 400; line-height: 31px; white-space: normal; }
  .intro strong { color: var(--orange); font-weight: 600; }
  .booking { left: 140px; top: 1072px; width: 666px; text-align: center; color: var(--white);
    font-size: 16px; font-weight: 500; }
  .booking strong { color: var(--orange); font-weight: 700; }

  .contact { color: var(--navy-deep); font-size: 25px; font-weight: 700; top: 1144px; }
  .icon { position: absolute; }
</style>
</head>
<body>
<main class="flyer">
  <svg class="backdrop" width="848" height="1200" viewBox="0 0 848 1200">
    <defs>
      <linearGradient id="crewScene" x1="0" y1="0" x2="1" y2="1">
        <stop offset="0" stop-color="#2b4b8a"/>
        <stop offset="0.55" stop-color="#1f3a75"/>
        <stop offset="1" stop-color="#1a3066"/>
      </linearGradient>
      <linearGradient id="vehicleTone" x1="0" y1="0" x2="0" y2="1">
        <stop offset="0" stop-color="#d8202f"/>
        <stop offset="0.25" stop-color="#e9e9eb"/>
        <stop offset="0.8" stop-color="#f7f7f8"/>
        <stop offset="1" stop-color="#6d7077"/>
      </linearGradient>
    </defs>
    <circle class="red-arc" cx="209" cy="888" r="640" fill="var(--red)"/>
    <circle class="crew-scene" cx="609" cy="784" r="591" fill="url(#crewScene)" role="img" aria-label="Paramedics in blue gloves attending to a patient"/>
    <path class="contact-band" d="M115,1108 L848,1108 L848,1200 L196,1200 Q150,1150 115,1108 Z" fill="var(--white)"/>
    <path class="vehicle-photo" d="M482,130 Q560,88 770,92 Q840,96 848,140 L848,420 Q800,436 760,430 L540,404 Q470,390 462,330 L466,230 Q470,160 482,130 Z" fill="url(#vehicleTone)" role="img" aria-label="White and red ambulance van, front three-quarter view"/>
  </svg>

  <div class="abs brand">
    <span class="brand-dot"></span>
    <span class="brand-name"><span class="main">CareSwift</span><span class="sub">Transit Health Services</span></span>
  </div>

  <div class="abs headline-we">We<span class="provides">Provide</span></div>
  <div class="abs headline-main">AMBULANCE</div>
  <div class="abs headline-amp">&amp;</div>
  <div class="abs headline-sub">Mobility Assistance</div>
  <div class="abs headline-tag">Vehicle Transportation Services</div>

  <!-- Health Facilities -->
  <svg class="icon icon-stethoscope" style="left:91px;top:695px" width="74" height="70" viewBox="0 0 74 70" fill="none" stroke="#fff" stroke-width="2.4" stroke-linecap="round">
    <path d="M6,4 L4,4 L4,24 Q4,40 18,40 Q32,40 32,24 L32,4 L30,4"/>
    <circle cx="6" cy="4" r="2.5"/><circle cx="30" cy="4" r="2.5"/>
    <path d="M18,40 L18,56 Q18,66 28,66 Q38,66 40,54 L44,30 Q46,20 54,22 Q60,24 60,32 L60,36"/>
    <circle cx="60" cy="42" r="6"/><circle cx="60" cy="42" r="2"/>
  </svg>
  <div class="abs service-title" style="left:179px;top:716px">Health Facilities</div>
  <span class="rule" style="left:156px;top:773px"></span>

  <!-- Standby Events -->
  <svg class="icon icon-pin" style="left:474px;top:687px" width="58" height="80" viewBox="0 0 58 80" fill="none" stroke="#fff" stroke-width="2.4" stroke-linejoin="round">
    <path d="M29,66 L20,54 Q2,46 2,29 A27,27 0 0 1 56,29 Q56,46 38,54 Z"/>
    <circle cx="29" cy="29" r="17"/>
    <path d="M25,20 H33 V25 H38 V33 H33 V38 H25 V33 H20 V25 H25 Z"/>
    <ellipse cx="29" cy="70" rx="25" ry="7"/>
  </svg>
  <div class="abs service-title" style="left:553px;top:711px">Standby Events</div>
  <span class="rule" style="left:542px;top:773px"></span>

  <!-- CPR Training -->
  <svg class="icon icon-cpr" style="left:91px;top:810px" width="78" height="88" viewBox="0 0 78 88" fill="none" stroke="#fff" stroke-width="2.4" stroke-linejoin="round" stroke-linecap="round">
    <circle cx="30" cy="10" r="9"/>
    <path d="M12,26 Q16,18 30,18 Q44,18 48,26 L50,58 L38,70 L22,70 L10,58 Z"/>
    <path d="M18,24 L30,58 L42,24"/>
    <path d="M4,74 L60,74 Q66,74 66,80 L66,84 L4,84 Q2,84 2,80 Z"/>
    <circle cx="66" cy="68" r="10"/>
  </svg>
  <div class="abs service-title" style="left:179px;top:827px">CPR Training</div>
  <div class="abs service-note" style="left:179px;top:860px">(cardiopulmonary</div>
  <div class="abs service-note" style="left:179px;top:883px">resuscitation)</div>
  <span class="rule" style="left:156px;top:920px"></span>

  <!-- Professional Education -->
  <svg class="icon icon-clipboard" style="left:474px;top:820px" width="64" height="76" viewBox="0 0 64 76" fill="none" stroke="#fff" stroke-width="2.4" stroke-linejoin="round" stroke-linecap="round">
    <rect x="2" y="8" width="60" height="66" rx="4"/>
    <path d="M22,8 L22,3 L42,3 L42,8 L46,12 L18,12 Z"/>
    <path d="M10,26 L14,30 L20,22"/>
    <path d="M26,24 H54 M26,30 H46"/>
    <path d="M14,48 L20,44 L26,48 L26,56 L20,60 L14,56 Z M26,48 L32,44 L38,48 L38,56 L32,60 L26,56 M20,60 L20,66 M38,52 L46,48"/>
    <circle cx="48" cy="40" r="3"/><circle cx="54" cy="48" r="2.5"/>
  </svg>
  <div class="abs service-title" style="left:553px;top:828px">Professional</div>
  <div class="abs service-title" style="left:553px;top:862px">Education courses</div>
  <span class="rule" style="left:542px;top:920px"></span>

  <p class="abs intro">We also provide healthcare training through<br>our training center such as <strong>CPR</strong> and other<br><strong>Education Courses.</strong></p>
  <p class="abs booking"><strong>Book your transport:</strong> call us or book online – we confirm your pickup time.</p>

  <!-- Contact -->
  <svg class="icon icon-phone" style="left:187px;top:1131px" width="45" height="45" viewBox="0 0 24 24">
    <path fill="var(--navy-deep)" d="M6.6 10.8a15.1 15.1 0 0 0 6.6 6.6l2.2-2.2c.3-.3.7-.4 1-.2 1.1.4 2.300.6 3.600.6.6 0 1 .4 1 1V20c0 .6-.4 1-1 1C10.6 21 3 13.400 3 4c0-.6.4-1 1-1h3.5c.6 0 1 .4 1 1 0 1.300.2 2.500.6 3.600.1.3 0 .7-.2 1z"/>
  </svg>
  <div class="abs contact" style="left:242px">+1 555 0142 77</div>

  <svg class="icon icon-globe" style="left:480px;top:1133px" width="54" height="54" viewBox="0 0 54 54" fill="none" stroke="var(--navy-deep)" stroke-width="3.4">
    <circle cx="27" cy="27" r="24"/>
    <ellipse cx="27" cy="27" rx="11" ry="24"/>
    <path d="M27,3 V51 M3,27 H51 M7,15 H47 M7,39 H47"/>
  </svg>
  <div class="abs contact" style="left:546px">www.careswift.com</div>
</main>
</body>
</html>
```